nonprofit organization looking for sleek new design

We need a fresh new look for this nonprofit organization, Tidewater Allies for Learning and Mutual Aid, INC (TALMA, Inc.). This organization provides educational, nutritional, dental health, and specialized services to Cedar Step children, aiming to support families meeting federal income poverty guidelines. Our mission is clear: "Creating a brighter future for the children and la familia." We focus on child development, family wellness, staff growth, and community partnerships.

```html
<!DOCTYPE html>
<html lang="en">
<head>
<meta charset="UTF-8">
<title>TALMA, Inc. — Creating a brighter future</title>
<link href="https://fonts.googleapis.com/css2?family=Lexend:wght@400;500;600;700&family=Open+Sans:wght@400;600;700&display=swap" rel="stylesheet">
<style>
:root{
  --blue:#1ba8d6;
  --blue-dark:#0d8fc0;
  --navy:#0f3550;
  --orange:#ff7a00;
  --orange-light:#ffa31a;
  --yellow:#f6b800;
  --ice:#e8f1f6;
  --text:#4a5560;
  --white:#ffffff;
}
*{margin:0;padding:0;box-sizing:border-box}
html,body{width:1200px;height:3889px;overflow:hidden;background:var(--white)}
body{position:relative;font-family:'Open Sans',sans-serif;color:var(--text)}
.abs{position:absolute}
.heading{font-family:'Lexend',sans-serif;font-weight:600;text-transform:uppercase;letter-spacing:1px}
.btn{position:absolute;display:flex;align-items:center;justify-content:center;font-family:'Lexend',sans-serif;font-weight:600;font-size:13px;text-transform:uppercase;color:var(--white);border-radius:3px}
.btn-orange{background:linear-gradient(90deg,var(--orange),var(--orange-light))}
.rule{position:absolute;height:3px;width:44px;background:var(--orange)}

/* header */
.site-header{position:absolute;top:0;left:0;width:1200px;height:79px;background:var(--white)}
.brand{position:absolute;left:101px;top:24px;font-family:'Lexend',sans-serif;font-weight:500;font-size:26px;color:var(--blue);letter-spacing:.5px}
.main-nav{position:absolute;left:337px;top:28px;display:flex}
.main-nav a{font-family:'Lexend',sans-serif;font-size:14px;color:var(--navy);text-decoration:none;text-transform:uppercase;margin-right:48px;position:relative}
.main-nav a.active::after{content:"";position:absolute;left:0;right:0;bottom:-11px;height:2px;background:var(--orange)}
.contact-btn{left:980px;top:14px;width:148px;height:42px;border-radius:21px;background:linear-gradient(90deg,var(--blue),var(--blue-dark))}

/* hero */
.hero{position:absolute;top:79px;left:0;width:1200px;height:630px;overflow:hidden}
.hero-photo{position:absolute;inset:0;background:linear-gradient(90deg,#c9c2c0 0%,#8fb7c8 30%,#3fa8cf 50%,#c7a57e 72%,#e1a35a 100%)}
.hero-badge{left:600px;top:117px;transform:translateX(-50%);height:35px;padding:0 14px;white-space:nowrap;background:var(--blue);color:var(--white);font-family:'Lexend',sans-serif;font-size:13px;display:flex;align-items:center;justify-content:center;text-transform:uppercase}
.hero-title{left:325px;top:160px;width:550px;text-align:center;color:var(--white);font-size:33px;line-height:38px;letter-spacing:1px}
.hero-btn{left:536px;top:291px;width:157px;height:45px}
.hero-arrow{position:absolute;top:240px}

/* about */
.about-frame{left:121px;top:802px;width:422px;height:360px;border:3px solid var(--blue);border-right:none}
.about-photo{left:134px;top:815px;width:505px;height:388px;background:linear-gradient(135deg,#9cc9ea,#6fa9d8 55%,#b58f74)}
.about-card{left:583px;top:862px;width:504px;height:362px;background:var(--white);box-shadow:0 10px 40px rgba(15,53,80,.12);padding:48px 38px 0 60px}
.about-card h2{font-size:29px;color:var(--navy)}
.about-card p{font-size:13.5px;line-height:23px;margin-top:14px}
.about-accent{background:linear-gradient(180deg,rgba(27,168,214,.12),rgba(27,168,214,.22))}

/* services */
.services{position:absolute;top:1341px;left:0;width:1200px;height:564px;background:var(--ice)}
.section-title{position:absolute;left:0;width:1200px;text-align:center;font-size:29px;color:var(--navy)}
.svc{position:absolute;width:272px;height:272px;border-radius:50%;overflow:hidden;display:flex;align-items:flex-end;justify-content:center;padding-bottom:40px}
.svc span{font-family:'Lexend',sans-serif;font-weight:600;color:var(--white);font-size:17px;text-transform:uppercase;text-align:center;line-height:20px;letter-spacing:.5px}
.svc-active{background:rgba(27,168,214,.92);flex-direction:column;justify-content:center;padding:0 40px;text-align:center}
.svc-active p{color:var(--white);font-size:12px;line-height:18px;margin-top:10px}

/* mission */
.mission{position:absolute;top:1905px;left:0;width:1200px;height:529px;overflow:hidden;background:linear-gradient(90deg,#ff6a00,#ffa10a)}
.mission h2{position:absolute;left:119px;top:105px;font-size:30px;color:var(--white)}
.mission h3{position:absolute;left:120px;top:186px;width:340px;font-size:18px;line-height:25px;color:var(--white);font-weight:700}
.mission p{position:absolute;left:120px;top:248px;width:410px;font-size:14.5px;line-height:24.5px;color:var(--white)}
.mission .outline-btn{left:119px;top:375px;width:156px;height:45px;border:2px solid var(--white);background:transparent}

/* focus */
.focus-card{position:absolute;width:235px;height:285px}
.focus-img{position:absolute;left:0;top:0;width:235px;height:160px}
.focus-body{position:absolute;left:7px;top:135px;width:221px;height:143px;background:var(--white);box-shadow:0 6px 18px rgba(0,0,0,.1);text-align:center;padding-top:18px}
.focus-body h4{font-family:'Open Sans',sans-serif;font-weight:600;font-size:17px;color:var(--navy);line-height:19px}
.focus-body p{font-size:11px;line-height:17px;margin:8px 16px 0;color:#6b737a}
.focus-body svg{margin-top:10px}
.focus-body.active{background:linear-gradient(180deg,var(--blue),#1596c8)}
.focus-body.active h4,.focus-body.active p{color:var(--white)}

/* cta */
.cta{position:absolute;top:2938px;left:0;width:1200px;height:528px}
.cta h2{position:absolute;left:137px;top:116px;font-size:34px;line-height:37px;color:var(--white)}
.cta p{position:absolute;left:139px;top:221px;width:480px;font-size:16.5px;line-height:27.5px;color:var(--white)}
.cta .btn{left:137px;top:379px;width:183px;height:53px;font-size:15px}

/* footer */
.site-footer{position:absolute;top:3466px;left:0;width:1200px;height:331px}
.f-divider{position:absolute;top:0;width:1px;height:250px;background:#e4e8eb}
.f-brand{left:130px;top:93px;font-family:'Lexend',sans-serif;font-weight:500;font-size:28px;color:var(--blue)}
.f-social{position:absolute;left:130px;top:140px;display:flex;flex-direction:column;gap:6px}
.f-social span{display:flex;align-items:center;gap:7px;font-size:12px;color:var(--text)}
.f-social i{display:block;width:10px;height:10px;border-radius:50%;background:var(--blue)}
.f-col h5{font-family:'Lexend',sans-serif;font-weight:600;font-size:16px;color:var(--navy);text-transform:uppercase;border-left:3px solid var(--orange);padding-left:20px;margin-left:-23px}
.f-col ul{list-style:none;margin-top:24px}
.f-col li{font-size:12.5px;color:var(--text);line-height:28px}
.f-contact{position:absolute;display:flex;gap:12px;font-size:12px;line-height:15px;color:var(--text)}
.f-contact b{display:block;font-weight:400;font-size:11.5px}
.f-contact .big{font-size:15px;color:var(--navy)}
.copyright{position:absolute;left:0;top:3797px;width:1200px;border-top:1px solid #e4e8eb;text-align:center;padding-top:30px;font-size:12px;color:#6b737a}
</style>
</head>
<body>

<header class="site-header">
  <div class="brand">TALMA, INC</div>
  <nav class="main-nav">
    <a class="active">About Us</a><a>Services</a><a>Programs</a><a>Blogs</a><a>Community</a>
  </nav>
  <div class="btn contact-btn">Contact Us</div>
</header>

<section class="hero">
  <div class="hero-photo" role="img" aria-label="Dentist with a smiling child on the left, mother helping a daughter draw on the right, blue tint in the middle"></div>
  <div class="abs hero-badge">Tidewater Allies for Learning and Mutual Aid</div>
  <h1 class="abs heading hero-title">Creating a brighter future for the children and la familia</h1>
  <div class="btn btn-orange hero-btn">Learn More</div>
  <svg class="hero-arrow" style="left:14px" width="30" height="50" viewBox="0 0 30 50"><path d="M24 6 L6 25 L24 44" stroke="#fff" stroke-width="5" fill="none"/></svg>
  <svg class="hero-arrow" style="left:1154px" width="30" height="50" viewBox="0 0 30 50"><path d="M6 6 L24 25 L6 44" stroke="#fff" stroke-width="5" fill="none"/></svg>
  <svg class="abs" style="left:600px;top:490px" width="20" height="30" viewBox="0 0 20 30"><path d="M10 2 V27 M2 19 L10 27 L18 19" stroke="#fff" stroke-width="2" fill="none"/></svg>
  <svg class="abs" style="left:0;top:560px" width="1200" height="70" viewBox="0 0 1200 70" preserveAspectRatio="none">
    <path d="M0 22 C200 70 420 50 640 30 C860 10 1060 0 1200 12 V70 H0Z" fill="#fff"/>
    <path d="M0 22 C200 70 420 50 640 30 C860 10 1060 0 1200 12" stroke="var(--yellow)" stroke-width="7" fill="none"/>
  </svg>
</section>

<section>
  <div class="abs about-frame"></div>
  <div class="abs about-photo" role="img" aria-label="Diverse hands joined in a circle against a blue sky"></div>
  <div class="abs about-accent" style="left:1087px;top:1050px;width:22px;height:200px" role="img" aria-label="Decorative dotted accent"></div>
  <div class="abs about-accent" style="left:895px;top:1224px;width:192px;height:26px" role="img" aria-label="Decorative dotted accent"></div>
  <div class="abs about-card">
    <h2 class="heading">About TALMA</h2>
    <div class="rule" style="position:relative;margin-top:6px"></div>
    <p>Lorem ipsum dolor sit amet, consectetur adipiscing elit, sed do eiusmod tempor incididunt ut labore et dolore magna aliqua. Ut enim ad minim veniam, quis nostrud exercitation ullamco laboris nisi ut aliquip ex ea commodo consequat.</p>
    <p>Duis aute irure dolor in reprehenderit in voluptate velit esse cillum dolore eu fugiat nulla pariatur.</p>
    <div class="btn btn-orange" style="position:relative;width:144px;height:42px;margin-top:14px;font-size:12px">Learn More</div>
  </div>
</section>

<section class="services">
  <h2 class="heading section-title" style="top:52px">Services Provide</h2>
  <div class="rule" style="left:578px;top:94px"></div>
  <div class="svc" style="left:98px;top:141px;background:linear-gradient(160deg,#cfb08c,#7a6a5a)" role="img" aria-label="Children reading books in class"><span>Educational</span></div>
  <div class="svc" style="left:359px;top:141px;background:linear-gradient(160deg,#e4c5a7,#b36a62)" role="img" aria-label="Smiling girl at a table with fresh fruit"><span>Nutritional</span></div>
  <div class="svc" style="left:864px;top:147px;background:linear-gradient(160deg,#b09178,#6a5446)" role="img" aria-label="Smiling volunteers handing out food"><span>Specialized<br>Services</span></div>
  <svg class="abs" style="left:588px;top:125px" width="312" height="312" viewBox="0 0 312 312"><circle cx="156" cy="156" r="152" fill="#fff" stroke="var(--blue)" stroke-width="3"/></svg>
  <div class="svc svc-active" style="left:608px;top:145px" role="img" aria-label="Smiling dentist, blue overlay">
    <span style="font-size:18px">Dental Health</span>
    <p>Lorem ipsum dolor sit amet, consectetur adipiscing elit, sed do eiusmod tempor</p>
    <svg width="30" height="30" viewBox="0 0 30 30" style="margin-top:12px"><circle cx="15" cy="15" r="13" stroke="#fff" stroke-width="1.5" fill="none"/><path d="M9 12 L15 18 L21 12" stroke="#fff" stroke-width="1.5" fill="none"/></svg>
  </div>
  <div class="btn btn-orange" style="left:516px;top:457px;width:182px;height:47px;font-size:14px">Learn More</div>
</section>

<section class="mission">
  <div class="abs" style="left:590px;top:0;width:700px;height:529px;background:linear-gradient(135deg,#d9cbb6,#8a7a6c 60%,#5e6876);clip-path:ellipse(620px 560px at 660px 264px)" role="img" aria-label="Young family playing with their daughter on the living room floor"></div>
  <svg class="abs" style="left:580px;top:0" width="160" height="529" viewBox="0 0 160 529"><path d="M130 0 C20 120 -10 380 150 529" stroke="var(--yellow)" stroke-width="4" fill="none"/></svg>
  <h2 class="heading">Our Mission</h2>
  <div class="rule" style="left:119px;top:149px;background:#fff"></div>
  <h3>Creating a brighter future for the children and la familia.</h3>
  <p>Lorem ipsum dolor sit amet, consectetur adipiscing elit, sed do eiusmod tempor incididunt ut labore et dolore magna aliqua. Ut enim ad minim veniam, quis nostrud exercitation ullamco laboris nisi ut aliquip ex ea</p>
  <div class="btn outline-btn">Learn More</div>
</section>

<section>
  <h2 class="heading section-title" style="top:2492px;color:var(--blue)">We Focus On</h2>
  <div class="rule" style="left:578px;top:2536px"></div>

  <div class="focus-card" style="left:106px;top:2576px">
    <div class="focus-img" style="background:linear-gradient(160deg,#b7896a,#e7cdb4)" role="img" aria-label="Mother and daughter playing with building blocks"></div>
    <div class="focus-body active" style="top:133px;height:150px">
      <h4>Child Development</h4>
      <p>Lorem ipsum dolor sit amet, consectetur adipiscing elit, sed do eiusmod tempor</p>
      <svg width="28" height="28" viewBox="0 0 28 28"><circle cx="14" cy="14" r="12.5" stroke="#fff" stroke-width="1.5" fill="none"/><path d="M9 12 L14 17 L19 12" stroke="#fff" stroke-width="1.5" fill="none"/></svg>
    </div>
  </div>
  <div class="focus-card" style="left:359px;top:2574px">
    <div class="focus-img" style="background:linear-gradient(180deg,#a9c8dc,#d9c3a4)" role="img" aria-label="Family running together on a beach"></div>
    <div class="focus-body">
      <h4>Family Wellness</h4>
      <p>Lorem ipsum dolor sit amet, consectetur adipiscing elit, sed do eiusmod tempor</p>
      <svg width="28" height="28" viewBox="0 0 28 28"><circle cx="14" cy="14" r="12.5" stroke="#c0392b" stroke-width="1.5" fill="none"/><path d="M9 12 L14 17 L19 12" stroke="#c0392b" stroke-width="1.5" fill="none"/></svg>
    </div>
  </div>
  <div class="focus-card" style="left:611px;top:2574px">
    <div class="focus-img" style="background:linear-gradient(160deg,#e8ecef,#7f8c97)" role="img" aria-label="Trainer presenting to staff at a whiteboard"></div>
    <div class="focus-body">
      <h4>Staff Growth</h4>
      <p>Lorem ipsum dolor sit amet, consectetur adipiscing elit, sed do eiusmod tempor</p>
      <svg width="28" height="28" viewBox="0 0 28 28"><circle cx="14" cy="14" r="12.5" stroke="#c0392b" stroke-width="1.5" fill="none"/><path d="M9 12 L14 17 L19 12" stroke="#c0392b" stroke-width="1.5" fill="none"/></svg>
    </div>
  </div>
  <div class="focus-card" style="left:860px;top:2574px">
    <div class="focus-img" style="background:linear-gradient(160deg,#a47a5e,#e2c7ae)" role="img" aria-label="Many hands stacked together in teamwork"></div>
    <div class="focus-body" style="padding-top:12px">
      <h4>Community<br>Partnerships</h4>
      <p>Lorem ipsum dolor sit amet, consectetur adipiscing</p>
      <svg width="28" height="28" viewBox="0 0 28 28"><circle cx="14" cy="14" r="12.5" stroke="#c0392b" stroke-width="1.5" fill="none"/><path d="M9 12 L14 17 L19 12" stroke="#c0392b" stroke-width="1.5" fill="none"/></svg>
    </div>
  </div>
</section>

<section class="cta">
  <svg class="abs" style="left:0;top:0" width="1200" height="528" viewBox="0 0 1200 528">
    <defs><linearGradient id="ctaGrad" x1="0" x2="1"><stop offset="0" stop-color="#1a9fd0"/><stop offset="1" stop-color="#27b7dc"/></linearGradient></defs>
    <path d="M0 0 H880 A278 264 0 0 1 880 528 H0Z" fill="url(#ctaGrad)"/>
    <circle cx="880" cy="263" r="213" fill="none" stroke="#fff" stroke-width="3"/>
  </svg>
  <div class="abs" style="left:672px;top:55px;width:416px;height:416px;border-radius:50%;background:linear-gradient(180deg,#86b9b4,#c9b99a 70%,#8e6c52)" role="img" aria-label="Child in aviator cap with cardboard wings pretending to fly"></div>
  <h2 class="heading">Start Building<br>Bright Future</h2>
  <div class="rule" style="left:139px;top:199px;background:#fff"></div>
  <p>Lorem ipsum dolor sit amet, consectetur adipiscing elit, sed do eiusmod tempor incididunt ut labore et dolore magna aliqua. Ut enim ad minim veniam, quis nostrud exercitation ullamco laboris nisi ut aliquip ex ea commodo consequat. Duis aute irure dolor in reprehend</p>
  <div class="btn btn-orange">Learn More</div>
</section>

<footer class="site-footer">
  <div class="f-divider" style="left:344px"></div>
  <div class="f-divider" style="left:590px;height:240px"></div>
  <div class="f-divider" style="left:799px;height:240px"></div>

  <div class="abs f-brand">TALMA, INC</div>
  <div class="f-social">
    <span><i></i>Kindlr</span>
    <span><i></i>Chirpa</span>
    <span><i></i>Snapfold</span>
  </div>

  <div class="abs f-col" style="left:370px;top:92px">
    <h5>Navigation</h5>
    <ul><li>About Us</li><li>The Community</li><li>Programs</li><li>News</li><li>Services</li></ul>
  </div>
  <div class="abs f-col" style="left:616px;top:92px">
    <h5>Resources</h5>
    <ul><li>Blogs</li><li>Support Us</li><li>Contact Us</li><li>Privacy Policy</li></ul>
  </div>
  <div class="abs f-col" style="left:828px;top:92px">
    <h5>Contact Us</h5>
  </div>
  <div class="f-contact" style="left:830px;top:136px">
    <svg width="22" height="22" viewBox="0 0 24 24"><path d="M6 3 L9 3 L10.5 8 L8.5 9.5 C9.5 12 12 14.5 14.5 15.5 L16 13.5 L21 15 L21 18 C21 19.5 19.5 21 18 21 C10 20 4 14 3 6 C3 4.5 4.5 3 6 3Z" fill="none" stroke="var(--blue)" stroke-width="1.6"/></svg>
    <div><b>Phone</b><span class="big">04-5550172</span></div>
  </div>
  <div class="f-contact" style="left:830px;top:184px">
    <svg width="22" height="24" viewBox="0 0 22 24"><path d="M11 23 C11 23 3 14 3 9 A8 8 0 0 1 19 9 C19 14 11 23 11 23Z" fill="var(--blue)"/><circle cx="11" cy="9" r="3" fill="#fff"/></svg>
    <div><b>Office</b>Harbor Lane 12, PO Box 4410 Norvale, 20415</div>
  </div>
  <div class="f-contact" style="left:830px;top:238px">
    <svg width="22" height="18" viewBox="0 0 22 18"><rect x="1" y="2" width="20" height="14" rx="1.5" fill="var(--blue)"/><path d="M1 3 L11 10 L21 3" stroke="#fff" stroke-width="1.5" fill="none"/></svg>
    <div><b>Email</b>hello@talma-allies.org</div>
  </div>
</footer>
<div class="copyright">Copyright © 2024 Tidewater Allies for Learning and Mutual Aid, INC</div>

</body>
</html>
```